Website for boutique digital agency helping high-tech startups accelerate growth.

We need a website design for a relatively young company based in Port Aster called 'LoomTrax'.

We are a professional services firm delivering digital infrastructure for revenue operations (RevOps)*.

Entrepreneurial startups and SMBs in the technology sector work with us to accelerate growth by delivering extraordinary customer experiences across the full customer lifecycle.

We would like a colourful design that utilises the (4) colours of our existing logo design.

The final design should communicate dynamic growth through relentless customer focus.
----------------------------------------------------------
*Revenue Operations (RevOps) is the strategic alignment of sales, marketing and customer success operations to accelerate growth by delivering extraordinary customer experiences across the full customer life cycle.
Updates

Target Market(s)

Entrepreneurial startups and SMBs (Small/Medium Businesses) in the technology sector.

Question: Why the technology sector?

Answer: Because technology entrepreneurs often have a tremendous challenge to effectively communicate to the market and to prospective customers the value and the benefits of their products & services due to the inherent complexity of technological innovation.

LoomTrax is a team of creatively-minded engineers and technologists who have worked with and understand the technologies and innovations our clients are passionate about bringing to market.

Industry/Entity Type

Professional Service

Number of Pages Required

5+ page

Font styles to use
Sans Serif

Requirements
Must have
• Minimalistic designs rich with visual meaning are highly preferred. Mobile responsive designs are also required. Must show how designs render on Desktop, Tablet and Smartphone devices.

Website pages:
1) Homepage: problem statement, target customers, value proposition & benefits
2) Services: 3-4 tiers of services packages with pricing and "how to work with us"
3) Resources: links to all kinds of relevant materials
4) Contact Us: contact form and special project quote form
5) Blog: matrix design with featured images for each post
Nice to have
• Bold, interesting, colourful, inspiring images that visually communicate:
- relentless customer focus
- extraordinary, memorable experiences
- business at the speed of innovation
Should not have
• Any meme or theme that panders to "political correctness".

```html
<!DOCTYPE html>
<html lang="en">
<head>
<meta charset="utf-8">
<title>LoomTrax — Digital infrastructure for RevOps</title>
<link href="https://fonts.googleapis.com/css2?family=Poppins:wght@300;400;500;600;700&display=swap" rel="stylesheet">
<style>
:root{
  --teal:#1b7b73;
  --teal-dark:#115e58;
  --teal-soft:#dcecec;
  --ink:#333a3d;
  --muted:#6f7678;
  --line:#d9dfe0;
  --white:#fff;
}
*{box-sizing:border-box;margin:0;padding:0}
html,body{width:1200px;height:4317px;overflow:hidden}
body{position:relative;background:var(--white);font-family:'Poppins',sans-serif;color:var(--ink)}
.abs{position:absolute}
.center{left:0;width:1200px;text-align:center}
.btn{position:absolute;display:flex;align-items:center;justify-content:center;background:var(--teal-dark);color:#fff;border-radius:30px;font-weight:600;font-size:11px;letter-spacing:.3px}
.btn-outline{background:#fff;color:var(--ink);border:1.5px solid var(--teal)}
.eyebrow{color:var(--teal);font-size:15px}
.section-title{font-size:38px;font-weight:600;color:#3a3f42}

/* header */
.hero-blob{top:0;left:540px}
.logo{top:40px;left:160px;font-size:20px;font-weight:600;color:#3a3f42;display:flex;align-items:center;gap:8px}
.logo-dot{width:26px;height:26px;border-radius:50%;background:var(--teal)}
.nav{top:42px;left:686px;display:flex;gap:26px;font-size:12px;font-weight:600;color:#fff}
.side-social{top:305px;left:72px;display:flex;flex-direction:column;align-items:center;gap:28px}
.side-social span{width:9px;height:9px;border-radius:50%;background:var(--teal)}
.side-social i{width:2px;height:22px;background:var(--teal)}
.hero-title{top:176px;left:157px;font-size:40px;font-weight:400;line-height:58px;color:#3a3f42}
.hero-title strong{display:block;font-size:56px;font-weight:700;line-height:54px}
.hero-sub{top:357px;left:160px;font-size:12px;line-height:19px;color:var(--muted);width:240px}
.hero-art{top:160px;left:578px;width:478px;height:334px;border-radius:18px;background:linear-gradient(135deg,#f1f4f6 0%,#e9eef0 40%,rgba(255,255,255,.0) 100%)}
.mouse{top:535px;left:570px;width:60px;height:60px;border-radius:50%;background:#fff;box-shadow:0 6px 18px rgba(0,0,0,.1);display:flex;align-items:center;justify-content:center}

/* why */
.why-title{top:672px;font-size:38px;font-weight:400;color:#3a3f42}
.why-title b{font-weight:700}
.why-text{top:735px;left:375px;width:450px;font-size:10px;line-height:17px;color:var(--muted)}
.video{top:821px;left:260px;width:680px;height:340px;background:linear-gradient(90deg,#c9cdcf 0%,#dfe2e3 45%,#c4b8b0 60%,#e6e8e9 100%)}
.play{top:962px;left:570px;width:60px;height:60px;border-radius:50%;border:2px solid #fff;display:flex;align-items:center;justify-content:center}

/* services */
.service-card{top:1416px;width:262px;height:332px;background:#fff;box-shadow:0 4px 20px rgba(0,0,0,.08)}
.service-card svg{position:absolute;top:40px;left:50%;transform:translateX(-50%)}
.service-card h3{position:absolute;top:128px;left:24px;font-size:12.5px;font-weight:600;color:#2f3436}
.service-card p{position:absolute;top:172px;left:24px;width:222px;font-size:10px;line-height:16.5px;color:var(--muted)}
.service-card .btn{top:292px;right:30px;width:70px;height:22px;font-size:8.5px}
.arrow-btn{top:1770px;width:40px;height:40px;border-radius:50%;background:#fff;box-shadow:0 3px 12px rgba(0,0,0,.1);display:flex;align-items:center;justify-content:center}

/* pricing */
.pricing-band{top:1865px;left:0;width:1200px;height:612px;background:var(--teal-soft)}
.price-card{top:2020px;width:277px;height:346px;background:#fff;border-radius:14px;text-align:center}
.price-card.featured{box-shadow:0 8px 24px rgba(0,0,0,.12)}
.price-card h3{margin-top:44px;font-size:19px;font-weight:400;color:#3a3f42}
.price-card p{margin:42px auto 0;width:220px;font-size:11.5px;line-height:19px;color:var(--muted)}
.price-card .price{margin-top:28px;font-size:23px;font-weight:600;color:var(--teal)}
.price-card .btn{left:75px;top:270px;width:127px;height:36px;font-size:12px;font-weight:500}
.dots{top:2418px;left:580px;display:flex;gap:9px;align-items:center}
.dots span{width:5px;height:5px;border-radius:50%;background:#9fbcbc}
.dots span.on{width:9px;height:9px;background:var(--teal)}

/* blog */
.post{top:2623px;width:278px;height:385px;background:#fff;box-shadow:0 3px 16px rgba(0,0,0,.08)}
.post .thumb{position:absolute;top:16px;left:16px;width:246px;height:168px}
.post h3{position:absolute;top:202px;left:16px;width:215px;font-size:17px;line-height:26px;font-weight:500;color:#2f3436}
.post .meta{position:absolute;top:264px;left:16px;font-size:9.5px;color:var(--muted)}
.post p{position:absolute;top:293px;left:16px;width:246px;font-size:10px;line-height:20px;color:var(--muted)}
.post a{position:absolute;top:351px;left:16px;font-size:10.5px;font-weight:600;color:var(--teal);text-decoration:none}

/* contact form */
.form-band{top:3089px;left:0;width:1200px;height:611px;background:var(--teal-soft)}
.form-card{top:3120px;left:310px;width:578px;height:580px;background:#fff}
.field{position:absolute;border-bottom:1px solid var(--line)}
.field label{display:block;font-size:10.5px;font-weight:600;color:#2f3436}
.field span{display:block;margin-top:9px;font-size:9.5px;color:#aab0b2}
.submit{top:3613px;left:350px;width:93px;height:34px;border-radius:3px;font-size:11px}

/* newsletter */
.news-title{top:3762px;font-size:25px;font-weight:400;color:#3a3f42}
.news-title b{font-weight:600}
.news-input{top:3823px;left:360px;width:322px;height:35px;background:#f1f3f4;font-size:8.5px;color:#a4aaac;padding:12px 22px}
.subscribe{top:3823px;left:704px;width:126px;height:35px;font-size:11.5px}

/* footer */
.footer-wave{top:3880px;left:0}
.foot-logo{top:4088px;left:180px;width:120px;text-align:center;color:#fff;font-size:18px;font-weight:600;line-height:24px}
.foot-logo .logo-dot{display:block;margin:0 auto 6px;background:#fff;width:32px;height:32px}
.stay{top:4174px;left:162px;font-size:23px;font-weight:500;color:#fff;line-height:30px}
.foot-social{top:4224px;left:172px;display:flex;gap:34px}
.foot-social span{width:10px;height:10px;border-radius:50%;background:#fff}
.foot-col{top:4103px;color:#fff}
.foot-col h4{font-size:15px;font-weight:500;margin-bottom:18px}
.foot-col li{list-style:none;font-size:12px;line-height:27px;display:flex;align-items:center;gap:8px}
</style>
</head>
<body>

<!-- header / hero -->
<svg class="abs hero-blob" width="660" height="530" viewBox="0 0 660 530" aria-hidden="true">
  <defs><linearGradient id="tealGrad" x1="0" y1="0" x2="1" y2="1"><stop offset="0" stop-color="#1f8a80"/><stop offset="1" stop-color="#146b64"/></linearGradient></defs>
  <path d="M20 0 H660 V520 C600 530 540 500 520 440 C500 380 470 330 400 300 C330 270 270 250 240 200 C210 150 160 150 100 140 C20 120 -10 50 20 0 Z" fill="url(#tealGrad)"/>
</svg>

<div class="abs logo"><span class="logo-dot"></span>loomtrax.io</div>
<nav class="abs nav"><span>HOME</span><span>SERVICES</span><span>RESOURCES</span><span>BLOG</span><span>CONTACT</span></nav>

<div class="abs side-social"><span></span><span></span><span></span><span></span><i></i></div>

<h1 class="abs hero-title">Delivering digital<br>infrastructure<strong>FOR RevOps.</strong></h1>
<p class="abs hero-sub">We drive growth through operational efficiency across the customer lifecycle.</p>
<div class="btn" style="top:410px;left:160px;width:162px;height:35px">LEARN MORE</div>

<div class="abs hero-art" role="img" aria-label="Illustration of a team of three working at desks with laptops beneath floating analytics dashboards"></div>

<div class="abs mouse"><svg width="20" height="30" viewBox="0 0 20 30" aria-hidden="true"><rect x="1" y="1" width="18" height="28" rx="9" fill="none" stroke="#8a9396" stroke-width="1.5"/><line x1="10" y1="6" x2="10" y2="12" stroke="#8a9396" stroke-width="1.5"/></svg></div>

<!-- why -->
<h2 class="abs center why-title">Why <b>LoomTrax??</b></h2>
<p class="abs why-text" style="text-align:center">Lorem ipsum dolor sit amet, consetetur sadipscing elitr, sed diam nonumy eirmod tempor invidunt ut labore et dolore magna aliquyam erat, sed diam voluptua. At vero eos et accusam et justo duo dolores et ea rebum. Stet clita kasd gubergren, no sea</p>
<div class="abs video" role="img" aria-label="Video still of a woman working on a laptop in a bright office"></div>
<div class="abs play"><svg width="18" height="20" viewBox="0 0 18 20" aria-hidden="true"><path d="M3 2 L16 10 L3 18 Z" fill="#fff"/></svg></div>
<div class="btn" style="top:1190px;left:540px;width:120px;height:34px;font-size:9px">SEE MORE</div>

<!-- services -->
<p class="abs center eyebrow" style="top:1297px">Our Services</p>
<h2 class="abs center section-title" style="top:1325px">What We Offer</h2>

<div class="abs service-card" style="left:184px">
  <svg width="70" height="62" viewBox="0 0 70 62" aria-hidden="true" fill="none" stroke="#1b7b73" stroke-width="2"><circle cx="30" cy="10" r="7"/><path d="M18 32 C18 22 42 22 42 32"/><rect x="6" y="30" width="22" height="28"/><line x1="11" y1="38" x2="23" y2="38"/><line x1="11" y1="45" x2="23" y2="45"/><line x1="11" y1="52" x2="23" y2="52"/><circle cx="52" cy="44" r="10"/><circle cx="52" cy="44" r="4"/></svg>
  <h3>CUSTOMER SUCCESS</h3>
  <p>Lorem ipsum dolor sit amet, consetetur sadipscing elitr, sed diam nonumy eirmod tempor invidunt ut labore et dolore magna aliquyam erat, sed diam voluptua. At vero</p>
  <div class="btn">SEE MORE</div>
</div>
<div class="abs service-card" style="left:469px">
  <svg width="70" height="62" viewBox="0 0 70 62" aria-hidden="true" fill="none" stroke="#1b7b73" stroke-width="2"><rect x="4" y="4" width="52" height="38"/><line x1="30" y1="42" x2="20" y2="58"/><line x1="30" y1="42" x2="40" y2="58"/><rect x="12" y="26" width="5" height="10"/><rect x="21" y="20" width="5" height="16"/><circle cx="44" cy="24" r="10"/><line x1="51" y1="31" x2="62" y2="42"/></svg>
  <h3>SALES</h3>
  <p>Lorem ipsum dolor sit amet, consetetur sadipscing elitr, sed diam nonumy eirmod tempor invidunt ut labore et dolore magna aliquyam erat, sed diam voluptua. At vero eos et accusam et justo duo dolores et ea rebum. Stet clita kasd gubergren, no sea takimata</p>
  <div class="btn">SEE MORE</div>
</div>
<div class="abs service-card" style="left:754px">
  <svg width="70" height="62" viewBox="0 0 70 62" aria-hidden="true" fill="none" stroke="#1b7b73" stroke-width="2"><rect x="4" y="4" width="62" height="42"/><line x1="4" y1="38" x2="66" y2="38"/><polyline points="12,30 24,18 34,26 46,12 56,18"/><line x1="35" y1="46" x2="35" y2="56"/><line x1="22" y1="57" x2="48" y2="57"/></svg>
  <h3>Marketing</h3>
  <p>Lorem ipsum dolor sit amet, consetetur sadipscing elitr, sed diam nonumy eirmod tempor invidunt ut labore et dolore magna aliquyam erat, sed diam voluptua. At vero eos et accusam et justo duo dolores et ea rebum</p>
  <div class="btn">SEE MORE</div>
</div>

<div class="abs arrow-btn" style="left:550px"><svg width="14" height="10" viewBox="0 0 14 10" aria-hidden="true"><path d="M13 5 H1 M5 1 L1 5 L5 9" stroke="#333" fill="none" stroke-width="1.3"/></svg></div>
<div class="abs arrow-btn" style="left:610px"><svg width="14" height="10" viewBox="0 0 14 10" aria-hidden="true"><path d="M1 5 H13 M9 1 L13 5 L9 9" stroke="#333" fill="none" stroke-width="1.3"/></svg></div>

<!-- pricing -->
<div class="abs pricing-band"></div>
<p class="abs center eyebrow" style="top:1895px;font-size:14px">Pricing</p>
<h2 class="abs center section-title" style="top:1922px">Our Pricing</h2>

<div class="abs price-card" style="left:126px">
  <h3>Gold Package</h3>
  <p>Lorem ipsum dolor sit amet, consectetur adipiscing elit. Aenean nisl nibh, sagittis ac faucibus sit</p>
  <div class="price">$ 2000</div>
  <div class="btn btn-outline">See Details</div>
</div>
<div class="abs price-card featured" style="left:459px">
  <h3>Platinum Package</h3>
  <p>Lorem ipsum dolor sit amet, consectetur adipiscing elit. Aenean nisl nibh, sagittis ac faucibus sit</p>
  <div class="price">$ 5000</div>
  <div class="btn">See Details</div>
</div>
<div class="abs price-card" style="left:793px">
  <h3>Silver Package</h3>
  <p>Lorem ipsum dolor sit amet, consectetur adipiscing elit. Aenean nisl nibh, sagittis ac faucibus sit</p>
  <div class="price">$ 1000</div>
  <div class="btn btn-outline">See Details</div>
</div>
<div class="abs dots"><span></span><span></span><span class="on"></span></div>

<!-- blog -->
<p class="abs center eyebrow" style="top:2534px;font-size:14px">Blog Posts</p>
<h2 class="abs center section-title" style="top:2560px">latest News</h2>

<article class="abs post" style="left:161px">
  <div class="thumb" role="img" aria-label="Photo of glowing blue network light trails" style="background:linear-gradient(135deg,#0b2a4a,#1f6fa8 50%,#0a1d33)"></div>
  <h3>Lorem ipsum dolor sit amet, consetetur</h3>
  <div class="meta">By Liam Hart Apr 8,2020</div>
  <p>Lorem ipsum dolor sit met, wrg consetetur sadipscing elitr, sed didfam nonumy emo.</p>
  <a href="#">View Details</a>
</article>
<article class="abs post" style="left:461px">
  <div class="thumb" role="img" aria-label="Photo of a dark blue digital network of connected points" style="background:linear-gradient(135deg,#0a1e36,#173d63 50%,#071526)"></div>
  <h3>Lorem ipsum dolor sit amet, consetetur</h3>
  <div class="meta">By Liam Hart Apr 8,2020</div>
  <p>Lorem ipsum dolor sit met, wrg consetetur sadipscing elitr, sed didfam nonumy emo.</p>
  <a href="#">View Details</a>
</article>
<article class="abs post" style="left:761px">
  <div class="thumb" role="img" aria-label="Photo of a dark tunnel with streaks of white light" style="background:radial-gradient(circle at 55% 50%,#9a9a9a,#2a2a2a 45%,#0b0b0b)"></div>
  <h3>Lorem ipsum dolor sit amet, consetetur</h3>
  <div class="meta">By Liam Hart Apr 8,2020</div>
  <p>Lorem ipsum dolor sit met, wrg consetetur sadipscing elitr, sed didfam nonumy emo.</p>
  <a href="#">View Details</a>
</article>

<!-- contact form -->
<div class="abs form-band"></div>
<div class="abs form-card"></div>
<div class="field" style="top:3162px;left:350px;width:232px;height:52px"><label>First Name</label><span>Ravi</span></div>
<div class="field" style="top:3162px;left:617px;width:234px;height:52px"><label>Last Name</label><span>Mohun</span></div>
<div class="field" style="top:3243px;left:350px;width:501px;height:54px"><label>Your Email Adress</label><span>ravimohun@mailbox.com</span></div>
<div class="field" style="top:3325px;left:350px;width:501px;height:54px"><label>Company</label><span>example</span></div>
<div class="field" style="top:3405px;left:350px;width:501px;height:54px"><label>Industry</label><span>example@.com</span></div>
<div class="field" style="top:3486px;left:350px;width:501px;height:101px"><label>Message</label><span>Lorem Ipsum is simply dummy text of the printing and.......</span></div>
<div class="btn submit">Submit</div>

<!-- newsletter -->
<p class="abs center eyebrow" style="top:3728px;font-size:14px">Newsletter</p>
<h2 class="abs center news-title">Do you want to get <b>Special News?</b></h2>
<div class="abs news-input">Drop Your Email</div>
<div class="btn subscribe">Subscribe</div>

<!-- footer -->
<svg class="abs footer-wave" width="1200" height="437" viewBox="0 0 1200 437" aria-hidden="true">
  <path d="M0 200 C120 110 210 40 330 50 C430 60 460 130 560 110 C660 90 700 10 820 20 C960 30 1060 110 1200 130 V437 H0 Z" fill="#1a7a72"/>
  <path d="M0 215 C150 150 260 140 380 170 C520 200 620 150 760 130 C900 110 1040 150 1200 150 V437 H0 Z" fill="#15706a"/>
</svg>
<div class="abs foot-logo"><span class="logo-dot"></span>loomtrax.io</div>
<div class="abs stay">Stay in touch</div>
<div class="abs foot-social"><span></span><span></span><span></span><span></span></div>

<div class="abs foot-col" style="left:441px"><h4>Quick Links</h4><ul><li>About</li><li>Home</li><li>Pricing</li><li>Location</li><li>Contact</li></ul></div>
<div class="abs foot-col" style="left:634px"><h4>Services</h4><ul><li>Marketing</li><li>Sales</li><li>Customer success</li></ul></div>
<div class="abs foot-col" style="left:855px"><h4>Contact</h4><ul>
  <li><svg width="11" height="11" viewBox="0 0 12 12" aria-hidden="true"><path d="M2 1 L4.5 1 L5.5 4 L4 5 C4.8 6.8 5.2 7.2 7 8 L8 6.5 L11 7.5 L11 10 C6 11 1 6 2 1 Z" fill="#fff"/></svg>000-000-0000</li>
  <li><svg width="11" height="9" viewBox="0 0 12 9" aria-hidden="true"><rect x="0.5" y="0.5" width="11" height="8" fill="#fff"/><path d="M0.5 0.5 L6 5 L11.5 0.5" stroke="#15706a" fill="none"/></svg>info@email.com</li>
  <li style="margin-top:12px"><svg width="10" height="13" viewBox="0 0 10 13" aria-hidden="true"><path d="M5 12 C5 12 1 7 1 4.5 A4 4 0 0 1 9 4.5 C9 7 5 12 5 12 Z" fill="#fff"/><circle cx="5" cy="4.5" r="1.5" fill="#15706a"/></svg>Port Aster</li>
</ul></div>

</body>
</html>
```